Elegant Business Cards & Letterhead

We will need the following that need to be designed: Letterhead and Business Cards, there winer will be re-hired for the balance of our stationary needs. Text for the cards and letterheads:

- Corporate Card instead of name
- landline: +971 (4) 362 7041
- mobile: +971 56 2819 605
- 800TUTOR
- email: dubai@velmora-lune.com
- www.velmora-lune.com
- PO Box 387261
Address: Castellan Heights Suite 1708, Dubai UAE

Thank you

Target Market(s)

VIPs, HNWI, High-end Families.

Industry/Entity Type

Luxury Market

Font styles to use
Other font styles liked:
• as explained

Colors

Designer to choose only greyscale colors for use in the design.

Requirements
Must have
• Elegant, Simple, Luxurious, Minimalistic
Nice to have
• Luxury, Golds, Engravings,
Should not have
• Much colors, funky,

```html
<!DOCTYPE html>
<html lang="en">
<head>
<meta charset="utf-8">
<title>Velmora Lune Letterhead</title>
<link href="https://fonts.googleapis.com/css2?family=Open+Sans:wght@400;600&display=swap" rel="stylesheet">
<style>
  :root {
    --backdrop: #cfd2d1;
    --paper: #ffffff;
    --ink: #0b0b0b;
    --gold: #d9a628;
    --gold-light: #f3cf3a;
    --gold-deep: #b8801f;
    --type-light: #f4f4f4;
  }
  * { margin: 0; padding: 0; box-sizing: border-box; }
  html, body {
    width: 1200px; height: 686px; overflow: hidden;
    background: var(--backdrop);
    font-family: "Open Sans", sans-serif;
  }
  .canvas {
    width: 1200px; height: 686px;
    display: flex; align-items: center; justify-content: center;
  }
  .letterhead {
    position: relative;
    width: 452px; height: 640px;
    background: var(--paper);
    box-shadow: 0 2px 10px rgba(0,0,0,0.12);
    overflow: hidden;
  }
  .brand-name {
    position: absolute;
    top: 52px; right: 44px;
    font-family: "Open Sans", sans-serif;
    font-weight: 400;
    font-size: 25px;
    letter-spacing: 3px;
    color: var(--gold);
    white-space: nowrap;
  }
  .contact-band {
    position: absolute;
    left: 0; right: 0; bottom: 0;
    height: 66px;
    background: var(--ink);
    border-top: 3px solid var(--gold-light);
    border-bottom: 3px solid var(--gold-light);
    display: flex;
    justify-content: space-between;
    align-items: center;
    padding: 0 16px;
    color: var(--type-light);
    font-size: 8.5px;
    line-height: 1.45;
  }
  .contact-band::before {
    content: "";
    position: absolute; left: 0; right: 0; top: -3px; height: 3px;
    background: linear-gradient(90deg, var(--gold-deep), var(--gold-light));
  }
  .contact-group { display: flex; align-items: center; gap: 6px; }
  .contact-icons { display: flex; flex-direction: column; gap: 3px; }
  .contact-icon { width: 9px; height: 9px; fill: var(--gold); display: block; }
  .contact-icon.pin { width: 11px; height: 13px; }
</style>
</head>
<body>
<main class="canvas">
  <section class="letterhead">
    <h1 class="brand-name">VELMORA LUNE</h1>

    <footer class="contact-band">
      <div class="contact-group phones">
        <div class="contact-icons">
          <svg class="contact-icon" viewBox="0 0 24 24" aria-hidden="true"><path d="M6.6 10.8a15 15 0 0 0 6.6 6.6l2.2-2.2a1 1 0 0 1 1-.25 11.4 11.4 0 0 0 3.6.57 1 1 0 0 1 1 1V20a1 1 0 0 1-1 1A17 17 0 0 1 3 4a1 1 0 0 1 1-1h3.5a1 1 0 0 1 1 1c0 1.25.2 2.45.57 3.57a1 1 0 0 1-.25 1z"/></svg>
          <svg class="contact-icon" viewBox="0 0 24 24" aria-hidden="true"><path d="M6.6 10.8a15 15 0 0 0 6.6 6.6l2.2-2.2a1 1 0 0 1 1-.25 11.4 11.4 0 0 0 3.6.57 1 1 0 0 1 1 1V20a1 1 0 0 1-1 1A17 17 0 0 1 3 4a1 1 0 0 1 1-1h3.5a1 1 0 0 1 1 1c0 1.25.2 2.45.57 3.57a1 1 0 0 1-.25 1z"/></svg>
        </div>
        <div class="contact-lines">
          <p>+971 (4) 362 7041</p>
          <p>+971 56 2819 605</p>
        </div>
      </div>

      <div class="contact-group online">
        <div class="contact-icons">
          <svg class="contact-icon" viewBox="0 0 24 24" aria-hidden="true"><circle cx="12" cy="12" r="10"/><path d="M2 12h20M12 2c3 3 3 17 0 20M12 2c-3 3-3 17 0 20" stroke="#0b0b0b" stroke-width="1.4" fill="none"/></svg>
          <svg class="contact-icon" viewBox="0 0 24 24" aria-hidden="true"><path d="M2 5h20v14H2z"/><path d="M2 5l10 8 10-8" stroke="#0b0b0b" stroke-width="1.6" fill="none"/></svg>
        </div>
        <div class="contact-lines">
          <p>www.velmora-lune.com</p>
          <p>dubai@velmora-lune.com</p>
        </div>
      </div>

      <div class="contact-group address">
        <svg class="contact-icon pin" viewBox="0 0 24 28" aria-hidden="true"><path d="M12 1a8 8 0 0 0-8 8c0 6 8 14 8 14s8-8 8-14a8 8 0 0 0-8-8zm0 11a3 3 0 1 1 0-6 3 3 0 0 1 0 6z"/><ellipse cx="12" cy="25.5" rx="7" ry="1.8"/></svg>
        <div class="contact-lines">
          <p>Castellan Heights Suite 1708,</p>
          <p>PO Box 387261, Dubai UAE</p>
        </div>
      </div>
    </footer>
  </section>
</main>
</body>
</html>
```